Car Soap Label Design specifically targeting RVs

I am private labeling a car wash soap to specifically target the RV industry. It will be sold in a one gallon jug with a 6"x11" spot to place the label on front and wrap around the two sides. (see attached pics for example of label size) The front of the label I want to have a realistic picture of a high dollar class A RV somehow integrated into the design, and the key features of the soap. I had wordsmithbot design a couple that I kind of like the look of that I will attach, but open to other options. I want something clean and professional looking that will back the premium product I am selling.
The name of my brand is "Blue Harbor Gleam". I want the brand name to be somewhere on the label, but not a main focus. I want the focus to be the product and its benefits. "Premium RV Wash and Wax" as the main verbiage. Benefits... "Developed for Use With Foam Gun or Bucket with Water", "Safe for All RV Exteriors", "Protective Wax Formula", "Enhanced Shine", "Water Repellent", "Streak Free Rinse", "UV Protection". On the side...Directions: 2 Ways of Mixing... Pour Concentrate into Foam Gun Bottle OR Mixing Ratio: 1 Part Wash & Wax / 3 Parts Water in bucket. Apply soap to one side of RV at a time and use carwash brush to easily loosen road film and rinse clean. On the other side... Keep from freezing, Keep Out of Reach of Children. MADE IN USA. Hazardous Ingredients: NONE . NOTICE: The seller and/or manufacturer assumes no responsibility for damage or injury resulting from misuse of this product. No warranties, expressed or implied, are given for the performance or safety of this product.

Target Market(s)

RV industry

Industry/Entity Type

RV/Auto

Requirements
Must have
• Clean, Professional look, size 6" tall and 11" wide
Nice to have
• Realistic Class A RV as part of design

```html
<!DOCTYPE html>
<html lang="en">
<head>
<meta charset="utf-8">
<title>Premium RV Wash and Wax – Label</title>
<link href="https://fonts.googleapis.com/css2?family=Montserrat:wght@400;500;600;700;800;900&display=swap" rel="stylesheet">
<style>
  :root{
    --page:#dcdcdc;
    --navy:#2b2e6b;
    --blue:#3f7fc4;
    --sky:#5fb4e8;
    --deep:#27408c;
    --notice:#4a86c8;
    --silver-1:#ffffff;
    --silver-2:#d9d9dc;
    --ink:#1d1d22;
    --white:#ffffff;
  }
  *{margin:0;padding:0;box-sizing:border-box}
  html,body{width:1200px;height:1117px;overflow:hidden;background:var(--page);font-family:"Montserrat",sans-serif}
  .label{
    position:absolute;left:59px;top:263px;width:1082px;height:591px;overflow:hidden;
    background:linear-gradient(180deg,var(--silver-1) 0%,var(--silver-2) 100%);
    box-shadow:6px 10px 18px rgba(0,0,0,.28);
  }
  .label-art{position:absolute;inset:0}
  .abs{position:absolute}
  .center{text-align:center}

  .directions-pill{
    left:36px;top:63px;width:184px;height:34px;border-radius:17px;
    background:var(--navy);color:var(--white);font-weight:800;font-size:19px;
    display:flex;align-items:center;justify-content:center;letter-spacing:.3px;
    box-shadow:0 3px 0 var(--sky);
  }
  .ways{left:27px;top:108px;display:flex;align-items:flex-end;gap:6px}
  .ways-num{font-size:86px;font-weight:800;color:var(--blue);line-height:.8}
  .ways-words{display:flex;flex-direction:column;line-height:1}
  .ways-big{font-size:43px;font-weight:800;color:var(--blue)}
  .ways-small{font-size:27px;font-weight:800;color:var(--navy);margin-top:2px}
  .mix-ratio{left:14px;top:201px;width:230px;font-size:11.6px;font-weight:700;color:var(--blue);line-height:16.2px}
  .apply{left:24px;top:276px;width:210px;font-size:11.6px;font-weight:400;color:var(--ink);line-height:16.2px}

  .side-name{left:20px;top:516px;width:218px;color:var(--white);line-height:1}
  .side-name-big{font-size:27px;font-weight:800}
  .side-name-small{font-size:18.5px;font-weight:700;margin-top:1px}

  .title{left:290px;top:34px;width:500px;color:var(--white);line-height:1}
  .title-big{font-size:54px;font-weight:800;letter-spacing:-.5px;text-shadow:0 2px 3px rgba(0,0,0,.35)}
  .title-mid{font-size:35px;font-weight:800;margin-top:5px;text-shadow:0 2px 3px rgba(0,0,0,.35)}
  .title-tag{font-size:12.5px;font-weight:600;letter-spacing:5.6px;margin-top:10px}

  .benefits{list-style:none;color:var(--white);font-weight:700;font-size:12.4px;line-height:14.5px}
  .benefits li{position:relative;padding-left:29px;margin-bottom:9px}
  .benefits li svg{position:absolute;left:0;top:1px}
  .benefits-a{left:310px;top:473px;width:240px}
  .benefits-a li:nth-child(1){margin-bottom:11px}
  .benefits-a li:nth-child(2){margin-bottom:10px}
  .benefits-b{left:554px;top:479px;width:240px}
  .benefits-b li{margin-bottom:7px}

  .warn-icon{left:933px;width:46px;height:46px}
  .warn-text{left:876px;width:160px;font-size:16.5px;font-weight:800;color:var(--navy);line-height:18.8px}
  .hazard{left:856px;top:296px;width:200px;font-size:12.6px;font-weight:700;color:var(--blue)}
  .notice{
    left:851px;top:331px;width:208px;height:172px;border-radius:10px;background:var(--notice);
    color:var(--white);font-size:11.7px;font-weight:600;line-height:15.4px;padding:18px 8px 0;
    box-shadow:0 4px 8px rgba(0,0,0,.2);
  }
  .made{left:876px;top:548px;width:160px;font-size:17px;font-weight:700;color:var(--white)}
</style>
</head>
<body>
<div class="label">
  <svg class="label-art" width="1082" height="591" viewBox="0 0 1082 591">
    <defs>
      <linearGradient id="topBand" x1="0" x2="1">
        <stop offset="0" stop-color="#2b4a95"/><stop offset=".5" stop-color="#3d8fd8"/><stop offset="1" stop-color="#2b4a95"/>
      </linearGradient>
      <linearGradient id="scene" x1="0" y1="0" x2="1" y2="1">
        <stop offset="0" stop-color="#5b86b8"/><stop offset=".45" stop-color="#b9c6cf"/>
        <stop offset=".7" stop-color="#e9c98f"/><stop offset="1" stop-color="#6f747a"/>
      </linearGradient>
      <linearGradient id="titlePanel" x1="0" y1="0" x2="0" y2="1">
        <stop offset="0" stop-color="#3a8ad6"/><stop offset="1" stop-color="#2c5aa8"/>
      </linearGradient>
      <linearGradient id="floor" x1="0" y1="0" x2="0" y2="1">
        <stop offset="0" stop-color="#2a3f8e"/><stop offset=".6" stop-color="#2f5aa8"/><stop offset="1" stop-color="#3b7cc6"/>
      </linearGradient>
      <linearGradient id="vehicle" x1="0" y1="0" x2="0" y2="1">
        <stop offset="0" stop-color="#f1f3f5"/><stop offset=".6" stop-color="#c9ced4"/><stop offset="1" stop-color="#5d636b"/>
      </linearGradient>
    </defs>

    <rect x="0" y="0" width="1082" height="22" fill="url(#topBand)"/>
    <rect x="0" y="20" width="1082" height="3" fill="var(--sky)"/>

    <g role="img" aria-label="Photo of a mountain road at sunset behind the RV">
      <rect x="250" y="36" width="582" height="356" fill="url(#scene)"/>
    </g>

    <path d="M250 36 L300 36 C325 36 335 46 352 72 L388 130 C402 152 420 162 450 162 L632 162 C662 162 680 152 694 130 L730 72 C747 46 757 36 782 36 L832 36 L832 22 L250 22 Z" fill="#c9ccd2"/>
    <path d="M262 22 L305 22 C330 22 342 34 360 62 L394 120 C408 144 425 154 455 154 L627 154 C657 154 674 144 688 120 L722 62 C740 34 752 22 777 22 Z" fill="url(#titlePanel)" stroke="var(--sky)" stroke-width="3"/>

    <path d="M0 500 C80 470 190 415 290 398 Q541 368 792 398 C892 415 1002 470 1082 505 L1082 591 L0 591 Z" fill="url(#floor)"/>
    <path d="M0 500 C80 470 190 415 290 398 Q541 368 792 398 C892 415 1002 470 1082 505" fill="none" stroke="var(--sky)" stroke-width="3"/>

    <g role="img" aria-label="Photo of a white Class A motorhome, front three-quarter view">
      <rect x="362" y="152" width="346" height="300" rx="26" fill="url(#vehicle)"/>
    </g>
    <g role="img" aria-label="Smaller photo of the same white motorhome">
      <rect x="45" y="348" width="172" height="144" rx="14" fill="url(#vehicle)"/>
    </g>
  </svg>

  <div class="abs directions-pill">DIRECTIONS</div>
  <div class="abs ways">
    <span class="ways-num">2</span>
    <span class="ways-words"><span class="ways-big">WAYS</span><span class="ways-small">OF MIXING</span></span>
  </div>
  <p class="abs center mix-ratio">Pour Concentrate into<br>Foam Gun Bottle OR Mixing Ratio:<br>1 Part Wash &amp; Wax / 3 Parts<br>Water in bucket.</p>
  <p class="abs center apply">Apply soap to one side of RV<br>at a time and use carwash brush<br>to easily loosen road film and<br>rinse clean.</p>

  <div class="abs center side-name">
    <div class="side-name-big">PREMIUM RV</div>
    <div class="side-name-small">WASH AND WAX</div>
  </div>

  <div class="abs center title">
    <div class="title-big">PREMIUM RV</div>
    <div class="title-mid">WASH AND WAX</div>
    <div class="title-tag">BLUE HARBOR GLEAM</div>
  </div>

  <ul class="abs benefits benefits-a">
    <li><svg width="13" height="13" viewBox="0 0 13 13"><circle cx="6.5" cy="6.5" r="6.5" fill="var(--sky)"/><path d="M3.6 6.7l2 2 3.8-4" stroke="#fff" stroke-width="1.6" fill="none"/></svg>DEVELOPED FOR USE<br>WITH FOAM GUN OR BUCKET<br>WITH WATER</li>
    <li><svg width="13" height="13" viewBox="0 0 13 13"><circle cx="6.5" cy="6.5" r="6.5" fill="var(--sky)"/><path d="M3.6 6.7l2 2 3.8-4" stroke="#fff" stroke-width="1.6" fill="none"/></svg>SAFE FOR ALL RV EXTERIORS</li>
    <li><svg width="13" height="13" viewBox="0 0 13 13"><circle cx="6.5" cy="6.5" r="6.5" fill="var(--sky)"/><path d="M3.6 6.7l2 2 3.8-4" stroke="#fff" stroke-width="1.6" fill="none"/></svg>UV PROTECTION</li>
  </ul>
  <ul class="abs benefits benefits-b">
    <li><svg width="13" height="13" viewBox="0 0 13 13"><circle cx="6.5" cy="6.5" r="6.5" fill="var(--sky)"/><path d="M3.6 6.7l2 2 3.8-4" stroke="#fff" stroke-width="1.6" fill="none"/></svg>PROTECTIVE WAX FORMULA</li>
    <li><svg width="13" height="13" viewBox="0 0 13 13"><circle cx="6.5" cy="6.5" r="6.5" fill="var(--sky)"/><path d="M3.6 6.7l2 2 3.8-4" stroke="#fff" stroke-width="1.6" fill="none"/></svg>ENHANCED SHINE</li>
    <li><svg width="13" height="13" viewBox="0 0 13 13"><circle cx="6.5" cy="6.5" r="6.5" fill="var(--sky)"/><path d="M3.6 6.7l2 2 3.8-4" stroke="#fff" stroke-width="1.6" fill="none"/></svg>WATER REPELLENT</li>
    <li><svg width="13" height="13" viewBox="0 0 13 13"><circle cx="6.5" cy="6.5" r="6.5" fill="var(--sky)"/><path d="M3.6 6.7l2 2 3.8-4" stroke="#fff" stroke-width="1.6" fill="none"/></svg>STREAK FREE RINSE</li>
  </ul>

  <svg class="abs warn-icon" style="top:60px" viewBox="0 0 46 46" aria-hidden="true">
    <circle cx="23" cy="23" r="23" fill="var(--blue)"/>
    <g stroke="#fff" stroke-width="2.2" stroke-linecap="round">
      <path d="M23 11v24M12.6 17l20.8 12M12.6 29l20.8-12"/>
      <path d="M20 13l3 3 3-3M20 33l3-3 3 3"/>
    </g>
  </svg>
  <div class="abs center warn-text" style="top:114px">KEEP FROM<br>FREEZING</div>

  <svg class="abs warn-icon" style="top:173px" viewBox="0 0 46 46" aria-hidden="true">
    <circle cx="23" cy="23" r="23" fill="var(--blue)"/>
    <circle cx="23" cy="23" r="17" fill="none" stroke="#fff" stroke-width="2"/>
    <circle cx="23" cy="15" r="3" fill="none" stroke="#fff" stroke-width="1.8"/>
    <path d="M19 21h8v8h-2v6h-4v-6h-2z" fill="none" stroke="#fff" stroke-width="1.8"/>
    <path d="M11 35L35 11" stroke="#fff" stroke-width="2"/>
  </svg>
  <div class="abs center warn-text" style="top:223px">KEEP OUT<br>OF REACH OF<br>CHILDREN</div>

  <p class="abs center hazard">Hazardous Ingredients: NONE</p>
  <p class="abs center notice">NOTICE: The seller and/or manufacturer assumes no responsibility for damage or injury resulting from misuse of this product. No warranties, expressed or implied, are given for the performance or safety of this product.</p>
  <p class="abs center made">MADE IN USA</p>
</div>
</body>
</html>
```